Professional & Modern Technology Business Card

We need a business card for our software/technology firm. Our services include Program/Project Management, Project Controls and Enterprise Analytics. Our clients are usually in the Aviation, Public Works, Transportation and Electric & Water Utility industries. We serve both public and private clients. Would like a very professional, conservative but somewhat modern design. Design, Develop, Deploy is the corporate tagline. We have two offices. The headquarters is in Atlanta, GA and a satellite office In Savannah, GA. Corporate Logo Attached.
Looking to do website and corporate brochure after the successful completion of this project. Would like to begin a working relationship with best designers.
Tagline: Design, Develop, Deploy
Website: www.quelvanesystems.example
My Name: Marla Dunstead
My Title: CEO
Email: mdunstead@quelvanesystems.example
Atlanta Address:
87 Corliss Avenue, #2291
Atlanta, GA 30301
Office: 404.555.0182
Fax: 404.555.0147
Mobile: 404.555.0163
Savannah Address:
350 West Harrow Bend Road
Suite 720
Savannah, GA 31401
Office: 912.555.0139
Fax: 404.555.0147
Mobile: 404.555.0163
Updates
Please include the email address in your designs: mdunstead@quelvanesystems.example.
I appreciate everyone's design efforts. Just a few notes:
1. Please remove the mobile number from the cards
2. The backs of the cards can be utilized for writing notes. Make sure your design on the back of the card is conducive to clearly adding writing if needed.
3. No black backgrounds please
4. Only use the corporate logo on the front of the card. You can use portions of the logo design, but not the logo in totality.
Thank You
Industry/Entity Type
Conservative
Look and feel
Each slider illustrates characteristics of the customer's brand and the style your logo design should communicate.

```html
<!DOCTYPE html>
<html lang="en">
<head>
<meta charset="utf-8">
<title>Quelvane Systems, Inc. — Business Card</title>
<link rel="stylesheet" href="https://fonts.googleapis.com/css2?family=Questrial&family=Roboto:wght@500;700&display=swap">
<style>
  :root {
    --page-bg: #e6e9ea;
    --ink-gray: #6b6c6f;
    --ink-soft: #7a7b7e;
    --brand-green: #8cb83a;
    --brand-green-dark: #7aa42c;
    --back-green: #9cc447;
    --back-green-light: #b0d165;
    --ink-white: #ffffff;
  }
  * { box-sizing: border-box; margin: 0; padding: 0; }
  html, body { width: 1200px; height: 960px; overflow: hidden; }
  body {
    background: var(--page-bg);
    font-family: "Questrial", "Helvetica Neue", Arial, sans-serif;
    position: relative;
  }
  .card {
    position: absolute;
    left: 250px;
    width: 700px;
    height: 400px;
    border-radius: 4px;
    box-shadow: 0 6px 20px rgba(0,0,0,0.14);
    overflow: hidden;
  }
  /* ---------- front ---------- */
  .card-front {
    top: 60px;
    background: radial-gradient(circle at 30% 70%, #ffffff 0%, #fafafa 55%, #f3f3f3 100%);
  }
  .accent-bar {
    position: absolute;
    right: 22px; top: 0;
    width: 10px; height: 120px;
    background: var(--brand-green);
  }
  .identity {
    position: absolute;
    right: 48px; top: 36px;
    text-align: right;
  }
  .person-name {
    font-family: "Roboto", Arial, sans-serif;
    font-weight: 700;
    font-size: 38px;
    color: var(--ink-gray);
    letter-spacing: -0.5px;
    line-height: 1;
  }
  .person-title {
    font-size: 17px;
    color: var(--ink-soft);
    margin-top: 4px;
  }
  .contact-lines {
    position: absolute;
    right: 48px; top: 140px;
    text-align: right;
    font-size: 14px;
    line-height: 1.45;
    color: var(--ink-soft);
  }
  .contact-lines .label {
    font-family: "Roboto", Arial, sans-serif;
    font-weight: 700;
    color: var(--brand-green);
  }
  .brand-lockup {
    position: absolute;
    left: 60px; top: 150px;
    display: flex;
    align-items: center;
    gap: 14px;
  }
  .brand-dot {
    width: 52px; height: 52px;
    border-radius: 50%;
    background: var(--brand-green);
    flex: none;
  }
  .brand-name {
    font-size: 34px;
    color: var(--ink-gray);
    line-height: 1.05;
  }
  .office {
    position: absolute;
    font-style: normal;
    font-size: 13.5px;
    line-height: 1.5;
    color: var(--ink-soft);
  }
  .office-title {
    font-family: "Roboto", Arial, sans-serif;
    font-weight: 700;
    color: var(--brand-green);
  }
  .office-atlanta { left: 34px; top: 284px; }
  .office-savannah { left: 232px; top: 248px; }
  .tagline-front {
    position: absolute;
    right: 48px; top: 282px;
    font-family: "Roboto", Arial, sans-serif;
    font-weight: 700;
    font-size: 15px;
    color: var(--brand-green);
  }
  /* ---------- back: open space for handwritten notes ---------- */
  .card-back {
    top: 500px;
    background: radial-gradient(circle at 35% 45%, var(--back-green-light) 0%, var(--back-green) 65%, var(--brand-green) 100%);
    color: var(--ink-white);
  }
  .back-dot {
    position: absolute;
    left: 40px; top: 40px;
    width: 30px; height: 30px;
    border-radius: 50%;
    background: var(--ink-white);
  }
  .tagline-back {
    position: absolute;
    left: 0; right: 0; bottom: 40px;
    text-align: center;
    font-size: 22px;
    letter-spacing: 1.5px;
    color: var(--ink-white);
  }
</style>
</head>
<body>

<section class="card card-front" aria-label="Business card front">
  <div class="accent-bar"></div>

  <div class="identity">
    <div class="person-name">Marla Dunstead</div>
    <div class="person-title">CEO</div>
  </div>

  <div class="contact-lines">
    <div><span class="label">web:</span> www.quelvanesystems.example</div>
    <div><span class="label">mail:</span> mdunstead@quelvanesystems.example</div>
  </div>

  <div class="brand-lockup">
    <span class="brand-dot"></span>
    <span class="brand-name">Quelvane<br>Systems, Inc.</span>
  </div>

  <address class="office office-savannah">
    <div class="office-title">Savannah Address:</div>
    350 West Harrow Bend Road<br>
    Suite 720<br>
    Savannah, GA 31401<br>
    Office: 912.555.0139<br>
    Fax: 404.555.0147
  </address>

  <address class="office office-atlanta">
    <div class="office-title">Atlanta Address:</div>
    87 Corliss Avenue, #2291<br>
    Atlanta, GA 30301<br>
    Office: 404.555.0182<br>
    Fax: 404.555.0147
  </address>

  <div class="tagline-front">Design, Develop, Deploy</div>
</section>

<section class="card card-back" aria-label="Business card back">
  <span class="back-dot"></span>
  <div class="tagline-back">Design, Develop, Deploy</div>
</section>

</body>
</html>
```